Storm Restoration Contractor needs a professional business card design

Looking for a professional business card design. Not looking for your cheapo MS Word standard ones that are readily available. Dont want it to be cookie cutter look like ones readily available online. We just recently changed our logo and want to freshen up all our documents. Our company handles restoring a property back to a pre-loss condition after a storm damages it. For example, wind, hail, flood, fire losses.

Target Market(s)

Property Owners, Homeowners, Property Owners, Commercial Property Owners, Property Management Companies, Hail and Wind Damaged Properties

Industry/Entity Type

Construction Company

Contact Information for Business Card

Brightline Facades
847-555-0193
847-555-0147 fax
www.brightlinefacades.example
info@brightlinefacades.example

Requirements
Must have
• Clean, Professional, fresh look
• Storm Restoration, Roofing, Siding, Windows
Nice to have
• If there is a way to incorporate storms that may be cool.

```html
<!DOCTYPE html>
<html lang="en">
<head>
<meta charset="utf-8">
<title>Brightline Facades — Business Card</title>
<link rel="stylesheet" href="https://fonts.googleapis.com/css2?family=Tangerine:wght@700&display=swap">
<style>
  :root {
    --backdrop: #80869a;
    --card: #595a68;
    --card-edge: #6c6d7b;
    --ink: #f2f2f4;
    --ink-soft: #d9d9de;
    --hole: #ffffff;
  }
  html, body {
    margin: 0;
    padding: 0;
    overflow: hidden;
  }
  body {
    width: 751px;
    height: 1200px;
    background: var(--backdrop);
    position: relative;
    font-family: "Tangerine", cursive;
    font-weight: 700;
  }
  .card {
    position: absolute;
    left: 26px;
    top: 53px;
    width: 693px;
    height: 1105px;
    background: var(--card);
    border: 2px solid var(--card-edge);
    border-radius: 40px;
    box-sizing: border-box;
  }
  .hang-hole {
    position: absolute;
    left: 404px;
    top: 229px;
    width: 54px;
    height: 54px;
    border-radius: 50%;
    background: var(--hole);
  }
  .brand-name,
  .services,
  .contact {
    position: absolute;
    left: 26px;
    width: 693px;
    margin: 0;
    text-align: center;
    line-height: 1;
    white-space: nowrap;
  }
  .brand-name {
    top: 330px;
    color: var(--ink);
    font-size: 108px;
    font-weight: 700;
  }
  .services {
    top: 478px;
    font-size: 52px;
    color: var(--ink-soft);
  }
  .contact-phone {
    top: 612px;
    font-size: 66px;
    color: var(--ink);
  }
  .contact-web {
    top: 770px;
    font-size: 62px;
    color: var(--ink-soft);
  }
  .contact-email {
    top: 900px;
    font-size: 62px;
    color: var(--ink-soft);
  }
</style>
</head>
<body>
  <div class="card"></div>
  <div class="hang-hole"></div>
  <h1 class="brand-name">Brightline Facades</h1>
  <p class="services">Storm Restoration, Roofing, Siding, Windows</p>
  <p class="contact contact-phone">847-555-0193, 847-555-0147 Fax</p>
  <p class="contact contact-web">www.brightlinefacades.example</p>
  <p class="contact contact-email">info@brightlinefacades.example</p>
</body>
</html>
```